Business card design needed

Want the logo on a medium blue background and a nice funky design. I have my own gym and run one on one personal training and nutrition sessions. want it to look lively.
Updates

Please note I requested my logo on a blue background 

PLEASE NOTE: I already have a logo. It is attached to the order!!

Target Market(s)

over 55s

Industry/Entity Type

Nutrition

Contact Information for Business Card

Front of card : Logo ( on blue background )
Keldra Ashby
Nutrition & Fitness Coach for Seniors
Private gym at : 17 Tindal Crescent, Wembury, Perth, WA 6166
Mob : 0418372651
Email : keldraashby@frelmo.com
"For Seniors by a Senior"

Back of card
B.A. ( Soc.)
Dip. Ed. (Sec.)
Wellness Coach
Cert 4 Personal Trainer
Cert. Nutritition
MOVE ON Facilitator
Ageing Boldly Moving Freely Facilitator
NLP Master

```html
<!DOCTYPE html>
<html lang="en">
<head>
<meta charset="utf-8">
<title>Silver Stride Nutrition &amp; Fitness – Business Card</title>
<link href="https://fonts.googleapis.com/css2?family=Open+Sans:wght@400&display=swap" rel="stylesheet">
<style>
  :root {
    --stage: #000000;
    --card-blue: #2a86cc;
    --card-glow: #4fb0e6;
    --card-edge: #1f74bb;
    --swirl-light: rgba(255,255,255,0.18);
    --text-white: #ffffff;
    --brand-gold: #f2e21c;
    --divider: #ffffff;
  }
  * { margin: 0; padding: 0; box-sizing: border-box; }
  html, body {
    width: 1200px; height: 1000px; overflow: hidden;
    background: var(--stage);
    font-family: "Open Sans", Arial, sans-serif;
  }
  .canvas { position: relative; width: 1200px; height: 1000px; }
  .card {
    position: absolute; width: 682px; height: 421px; overflow: hidden;
    color: var(--text-white);
  }
  .card-front { left: 136px; top: 59px; }
  .card-back { left: 383px; top: 511px; }
  .card-backdrop {
    position: absolute; inset: 0;
  }
  .card-front .card-backdrop {
    background:
      radial-gradient(circle at 200px 215px, var(--card-glow) 0, rgba(79,176,230,0) 190px),
      radial-gradient(circle at 600px 320px, var(--swirl-light) 0, rgba(255,255,255,0) 160px),
      linear-gradient(180deg, var(--card-blue), var(--card-edge));
  }
  .card-back .card-backdrop {
    background:
      radial-gradient(circle at 340px 90px, var(--card-glow) 0, rgba(79,176,230,0) 220px),
      radial-gradient(circle at 90px 280px, var(--swirl-light) 0, rgba(255,255,255,0) 150px),
      radial-gradient(circle at 590px 290px, var(--swirl-light) 0, rgba(255,255,255,0) 150px),
      linear-gradient(180deg, var(--card-blue), var(--card-edge));
  }
  .brand {
    position: absolute; text-align: center;
    color: var(--brand-gold); font-weight: 400;
  }
  .brand-dot {
    display: block; margin: 0 auto;
    border-radius: 50%; background: var(--brand-gold);
  }
  .brand-name { display: block; white-space: nowrap; }
  .card-front .brand { left: 92px; top: 150px; width: 220px; }
  .card-front .brand-dot { width: 40px; height: 40px; margin-bottom: 28px; }
  .card-front .brand-name { font-size: 26px; line-height: 34px; }
  .card-back .brand { left: 221px; top: 62px; width: 240px; }
  .card-back .brand-dot { width: 30px; height: 30px; margin-bottom: 14px; }
  .card-back .brand-name { font-size: 20px; line-height: 26px; }
  .contact-divider {
    position: absolute; left: 333px; top: 124px; width: 1px; height: 171px;
    background: var(--divider);
  }
  .contact-details {
    position: absolute; left: 348px; top: 118px;
    font-size: 17px; line-height: 26px; list-style: none;
  }
  .credentials {
    position: absolute; left: 0; top: 244px; width: 682px;
    text-align: center; font-size: 17px; line-height: 26px;
  }
</style>
</head>
<body>
<main class="canvas">
  <section class="card card-front">
    <div class="card-backdrop" role="img" aria-label="Medium blue background with soft light swirl pattern"></div>
    <div class="brand">
      <span class="brand-dot"></span>
      <span class="brand-name">Silver Stride</span>
      <span class="brand-name">Nutrition &amp; Fitness</span>
    </div>
    <div class="contact-divider"></div>
    <ul class="contact-details">
      <li>Keldra Ashby Nutrition &amp;</li>
      <li>Fitness Coach for Seniors</li>
      <li>Private gym at : 17 Tindal Crescent,</li>
      <li>Wembury, Perth, WA 6166</li>
      <li>Mob : 0418372651</li>
      <li>Email : keldraashby@frelmo.com</li>
      <li>"For Seniors by a Senior"</li>
    </ul>
  </section>

  <section class="card card-back">
    <div class="card-backdrop" role="img" aria-label="Medium blue background with soft light swirl pattern"></div>
    <div class="brand">
      <span class="brand-dot"></span>
      <span class="brand-name">Silver Stride</span>
      <span class="brand-name">Nutrition &amp; Fitness</span>
    </div>
    <div class="credentials">
      <p>B.A. ( Soc.) Dip. Ed. (Sec.)</p>
      <p>Wellness Coach Cert 4 Personal Trainer Cert.</p>
      <p>Nutritition MOVE ON Facilitator Ageing Boldly Moving Freely</p>
      <p>Facilitator NLP Master</p>
    </div>
  </section>
</main>
</body>
</html>
```